Branding for salad and dip containers - retail

we are trying to modernise our packaging design
the lids will be pre-printed (only with our logo) the design can be any shape, preferably not covering the whole top as we want the product to show
NO OTHER details are needed on the lid! Just the logo in bold modern design (using our existing logo and colours) fresh modern and bold
this is the container size we use
https://www.vessorix7.co.uk/acatalog/280ml-rectangular-clear-tamperproof-container-lid.html#SID=64
see images attached of some trials made that we don’t like
1) One has too many other details
2) The other has not utilised our brand and logo

Target Market(s)

Retail Customers

Industry/Entity Type

food

Requirements
Must have
• our current existing logo included
Nice to have
• i would like to see my logo rebranded in a modern sleek design ready to printed on container tops
Should not have
• none of the current add ons- just logo bold and modern

```html
<!DOCTYPE html>
<html lang="en">
<head>
<meta charset="utf-8">
<title>Harlowe's – Lid Label</title>
<link rel="stylesheet" href="https://fonts.googleapis.com/css2?family=Arvo:wght@400&display=swap">
<style>
  :root {
    --canvas-bg: #ece9e6;
    --label-white: #ffffff;
    --label-edge: #3bb0e0;
    --brand-red: #c4000b;
    --plaque-white: #ffffff;
    --plaque-outline: #2b2b2b;
    --ornament-tint: #f3d3d3;
    --name-ink: #2a2a2a;
  }
  * { margin: 0; padding: 0; box-sizing: border-box; }
  html, body {
    width: 1200px;
    height: 1200px;
    overflow: hidden;
    background: var(--canvas-bg);
  }
  .canvas {
    position: relative;
    width: 1200px;
    height: 1200px;
  }
  .lid-label {
    position: absolute;
    left: 100px;
    top: 220px;
    width: 1000px;
    height: 760px;
  }
  .brand-name {
    font-family: "Arvo", "Rockwell", serif;
    font-weight: 400;
    font-size: 92px;
    fill: var(--name-ink);
    letter-spacing: 1px;
  }
</style>
</head>
<body>
<main class="canvas">
  <svg class="lid-label" viewBox="0 0 1000 760" xmlns="http://www.w3.org/2000/svg">
    <!-- label base -->
    <rect class="label-base" x="2" y="2" width="996" height="756" rx="34" ry="34"
          fill="var(--label-white)" stroke="var(--label-edge)" stroke-width="4"/>

    <!-- red brand panel -->
    <rect class="brand-panel" x="38" y="36" width="924" height="688" rx="26" ry="26"
          fill="var(--brand-red)"/>

    <!-- white plaque with notched ends -->
    <path class="plaque" d="M150,96 H850 Q868,150 930,162 V598 Q868,610 850,664 H150 Q132,610 70,598 V162 Q132,150 150,96 Z"
          fill="var(--plaque-white)" stroke="var(--plaque-outline)" stroke-width="6" stroke-linejoin="round"/>

    <!-- scroll ornament areas -->
    <rect class="ornament-left" x="96" y="190" width="96" height="380" rx="40"
          fill="var(--ornament-tint)" role="img" aria-label="Red filigree scroll ornament, left end of plaque"/>
    <rect class="ornament-right" x="836" y="190" width="78" height="380" rx="36"
          fill="var(--ornament-tint)" role="img" aria-label="Red filigree scroll ornament, right end of plaque"/>

    <!-- brand circle -->
    <circle class="brand-dot" cx="440" cy="380" r="150" fill="var(--brand-red)"/>

    <!-- brand name, reading upward -->
    <text class="brand-name" x="0" y="0" text-anchor="middle"
          transform="translate(792 380) rotate(-90)">Harlowe's</text>
  </svg>
</main>
</body>
</html>
```